TriVex Business Card Design - double sided -plumbing local plumbing company

We have a Plumbing company where the design was create through Sketch Hive. We would now like a business card designed as well. We want it to be in the colour version of the logo.

Details below for the card.

Phone Number: 0438 615 247
Email: info@trivexplumbing.example.au
Website: https://trivexplumbing.example.au
We really want a sophisticated design that stand out from the other- informative and timeless.

Target Market(s)

local Canberra market

Industry/Entity Type

Plumbing, gas fitting, hot water

Contact Information for Business Card

Phone number, email, logo and "Supplying all your heating, cooling and hot water needs"

Requirements
Must have
• bust be colourful, must also be though about it being printed on a magnet. must Vex with the logo - I dont want the logo and information chucked onto a white canvas I would prefer it to be smooth and look purposeful

```html
<!DOCTYPE html>
<html lang="en">
<head>
<meta charset="utf-8">
<title>TriVex Plumbing – Business Card</title>
<link rel="stylesheet" href="https://fonts.googleapis.com/css2?family=Quicksand:wght@400;500;700&display=swap">
<style>
  :root {
    --bg: #dcdddd;
    --card: #ffffff;
    --blue: #4cc3ea;
    --blue-faint: #eaf7fd;
    --yellow: #f9cf5f;
    --yellow-deep: #f5a51b;
    --yellow-light: #fde08a;
  }
  * { margin: 0; padding: 0; box-sizing: border-box; }
  html, body {
    width: 1200px; height: 1200px; overflow: hidden;
    background: var(--bg);
    font-family: "Quicksand", sans-serif;
  }
  .sheet {
    width: 1200px; height: 1200px;
    display: flex; flex-direction: column; align-items: center; justify-content: center;
    gap: 72px;
  }
  .card {
    position: relative;
    width: 900px; height: 514px;
    background: var(--card);
    overflow: hidden;
    box-shadow: 0 10px 30px rgba(0,0,0,0.12);
  }

  /* Front – contact side */
  .card-front .name {
    position: absolute; left: 64px; top: 58px;
    font-size: 50px; font-weight: 700; letter-spacing: 1px;
    color: var(--blue);
  }
  .card-front .role {
    position: absolute; left: 66px; top: 116px;
    font-size: 22px; font-weight: 400; letter-spacing: 1px;
    color: var(--yellow);
  }
  .card-front .rule {
    position: absolute; left: 0; right: 0; top: 156px;
    height: 3px; background: var(--yellow);
  }
  .contact-list {
    position: absolute; left: 40px; top: 196px;
    list-style: none;
    display: flex; flex-direction: column; gap: 14px;
  }
  .contact-item {
    display: flex; align-items: center; gap: 22px;
    font-size: 21px; font-weight: 500; color: var(--blue);
  }
  .contact-icon { width: 26px; height: 26px; flex: none; }
  .watermark {
    position: absolute; right: 40px; bottom: -22px;
    font-size: 190px; font-weight: 700; letter-spacing: 2px;
    color: var(--blue-faint);
    line-height: 1;
  }

  /* Back – brand side */
  .card-back .band {
    position: absolute; inset: 0; width: 100%; height: 100%;
  }
  .brand {
    position: absolute; left: 150px; top: 170px;
    font-size: 150px; font-weight: 700; letter-spacing: 4px;
    color: #ffffff; line-height: 1;
  }
  .tagline {
    position: absolute; left: 156px; top: 344px;
    font-size: 21px; font-weight: 500;
    color: var(--blue);
  }
</style>
</head>
<body>
<main class="sheet">

  <section class="card card-front" aria-label="Business card front">
    <h1 class="name">YOUR NAME</h1>
    <p class="role">LOREM IPSUM</p>
    <div class="rule"></div>
    <ul class="contact-list">
      <li class="contact-item">
        <svg class="contact-icon" viewBox="0 0 26 26" aria-hidden="true">
          <circle cx="13" cy="13" r="13" fill="var(--yellow)"/>
          <path d="M9.5 7.5l2 2.2-1.2 1.5c.8 1.7 2 2.9 3.6 3.7l1.5-1.2 2.2 2-1.2 1.8c-3.8-.4-7.4-4-7.8-7.8z" fill="#fff"/>
        </svg>
        <span>0438 615 247</span>
      </li>
      <li class="contact-item">
        <svg class="contact-icon" viewBox="0 0 26 26" aria-hidden="true">
          <circle cx="13" cy="13" r="13" fill="var(--yellow)"/>
          <rect x="7" y="9" width="12" height="8.5" rx="1" fill="#fff"/>
          <path d="M7.5 9.5l5.5 4.3 5.5-4.3" fill="none" stroke="var(--yellow)" stroke-width="1.2"/>
        </svg>
        <span>info@trivexplumbing.example.au</span>
      </li>
      <li class="contact-item">
        <svg class="contact-icon" viewBox="0 0 26 26" aria-hidden="true">
          <circle cx="13" cy="13" r="13" fill="var(--yellow)"/>
          <g fill="none" stroke="#fff" stroke-width="1.3">
            <circle cx="13" cy="13" r="6"/>
            <ellipse cx="13" cy="13" rx="2.6" ry="6"/>
            <path d="M7 13h12"/>
          </g>
        </svg>
        <span>trivexplumbing.example.au</span>
      </li>
    </ul>
    <div class="watermark" aria-hidden="true">TriVex</div>
  </section>

  <section class="card card-back" aria-label="Business card back">
    <svg class="band" viewBox="0 0 900 514" preserveAspectRatio="none" aria-hidden="true">
      <defs>
        <linearGradient id="bandGradient" x1="0" y1="1" x2="1" y2="0">
          <stop offset="0" stop-color="var(--yellow-deep)"/>
          <stop offset="0.55" stop-color="var(--yellow)"/>
          <stop offset="1" stop-color="var(--yellow-light)"/>
        </linearGradient>
      </defs>
      <polygon points="0,0 900,0 900,95 330,514 0,514" fill="url(#bandGradient)"/>
    </svg>
    <div class="brand">TriVex</div>
    <p class="tagline">"Supplying all your heating, cooling and hot water needs"</p>
  </section>

</main>
</body>
</html>
```